The Plaster & Resonance Craftworks Inc (PRCI)

Create a LOGO and Business Card design.

Colors: Black, Bright Yellow & Red

Description of company: commercial carpentry, metal framing, drywall, taping/spackling, demolition, rough/finish carpentry.

Target Market(s)

developers, architects, general contractors, construction managers

Industry/Entity Type

Business

```html
<!DOCTYPE html>
<html lang="en">
<head>
<meta charset="UTF-8">
<title>PRCI Business Card</title>
<link rel="stylesheet" href="https://fonts.googleapis.com/css2?family=Russo+One&family=Play:wght@700&display=swap">
<style>
  :root {
    --card-black: #000000;
    --signal-yellow: #f5e616;
    --signal-red: #e8202a;
  }
  html, body {
    margin: 0;
    padding: 0;
    overflow: hidden;
    background: var(--card-black);
  }
  .card {
    position: relative;
    width: 1200px;
    height: 600px;
    background: var(--card-black);
    overflow: hidden;
  }
  .services {
    position: absolute;
    left: 18px;
    top: 14px;
    margin: 0;
    font-family: "Play", sans-serif;
    font-weight: 700;
    font-size: 20px;
    letter-spacing: 1.2px;
    word-spacing: 2px;
    color: var(--signal-yellow);
    white-space: nowrap;
  }
  .person-name {
    position: absolute;
    left: 18px;
    top: 54px;
    margin: 0;
    font-family: "Russo One", sans-serif;
    font-weight: 400;
    font-size: 36px;
    line-height: 1.1;
    color: var(--signal-yellow);
    text-shadow:
      2px 2px 0 var(--signal-red), -2px -2px 0 var(--signal-red),
      2px -2px 0 var(--signal-red), -2px 2px 0 var(--signal-red),
      0 2px 0 var(--signal-red), 2px 0 0 var(--signal-red),
      0 -2px 0 var(--signal-red), -2px 0 0 var(--signal-red);
  }
  .stripes {
    position: absolute;
    left: 0;
    top: 0;
  }
  .brand {
    position: absolute;
    left: 18px;
    top: 378px;
    height: 112px;
    display: flex;
    align-items: center;
    gap: 26px;
  }
  .brand-square {
    width: 96px;
    height: 96px;
    background: var(--signal-yellow);
  }
  .brand-name {
    font-family: "Play", sans-serif;
    font-weight: 700;
    font-size: 132px;
    line-height: 1;
    letter-spacing: 18px;
    color: var(--signal-yellow);
  }
  .brand-tagline {
    position: absolute;
    left: 656px;
    top: 467px;
    font-family: "Play", sans-serif;
    font-weight: 700;
    font-size: 20px;
    letter-spacing: 0.6px;
    color: var(--signal-yellow);
    white-space: nowrap;
  }
  .contact-row {
    position: absolute;
    left: 0;
    top: 525px;
    height: 37px;
    width: 1050px;
    font-family: "Play", sans-serif;
    font-weight: 700;
    font-size: 20px;
    color: var(--card-black);
  }
  .contact-label {
    position: absolute;
    top: 8px;
  }
  .contact-phone { left: 18px; }
  .contact-email { left: 358px; }
  .contact-web { left: 715px; }
</style>
</head>
<body>
  <div class="card">
    <p class="services">commercial carpentry, metal framing, drywall, taping/spackling, demolition, rough/finish carpentry.</p>
    <h1 class="person-name">Sam Rivera</h1>

    <svg class="stripes" width="1200" height="600" viewBox="0 0 1200 600" aria-hidden="true">
      <polygon class="stripe-red" fill="var(--signal-red)"
        points="0,500 1035,500 1200,356 1200,378 1042,517 0,517"/>
      <polygon class="stripe-yellow" fill="var(--signal-yellow)"
        points="0,525 1046,525 1200,392 1200,442 1062,562 0,562"/>
    </svg>

    <div class="brand">
      <span class="brand-square" aria-hidden="true"></span>
      <span class="brand-name">PRCI</span>
    </div>
    <span class="brand-tagline">Plaster &amp; Resonance Craftworks Inc.</span>

    <div class="contact-row">
      <span class="contact-label contact-phone">Phone:</span>
      <span class="contact-label contact-email">E-Mail:</span>
      <span class="contact-label contact-web">Web:</span>
    </div>
  </div>
</body>
</html>
```